Business cards for Marrowfield Consulting with the following info for the front side:

Marrowfield Consulting
Executive Coaching and Human Capital Strategy
www.marrowfield.example

Idalia Renvoort
Principal
idalia@marrowfield.example
+1 555 274 9186

Black background, text using the colours of the logo - enclosed.

The back side of the business card should feature the logo in the middle, with "Executive Coaching and Human Capital Strategy" on top and "www.marrowfield.example" below.

```html
<!DOCTYPE html>
<html lang="en">
<head>
<meta charset="utf-8">
<title>Marrowfield Consulting — Business Cards</title>
<link href="https://fonts.googleapis.com/css2?family=Montserrat:wght@400;500;700&display=swap" rel="stylesheet">
<style>
  :root {
    --stage: #262626;
    --stage-edge: #151515;
    --card: #111213;
    --card-soft: #17191b;
    --blue: #36a9e1;
    --yellow: #f6b90a;
    --white: #f2f2f2;
  }
  * { box-sizing: border-box; margin: 0; padding: 0; }
  html, body { width: 1200px; height: 900px; overflow: hidden; }
  body {
    background: radial-gradient(ellipse at 55% 30%, #343434 0%, var(--stage) 45%, var(--stage-edge) 100%);
    font-family: "Montserrat", Arial, sans-serif;
    display: flex;
    flex-direction: column;
    align-items: center;
    justify-content: center;
    gap: 44px;
  }
  .card {
    position: relative;
    width: 640px;
    height: 366px;
    background: linear-gradient(135deg, var(--card) 0%, var(--card-soft) 100%);
    box-shadow: 0 18px 40px rgba(0,0,0,.55);
    overflow: hidden;
  }
  .card__band {
    position: absolute;
    left: 0; right: 0; bottom: 0;
    height: 14px;
    background: var(--blue);
  }
  .brand { display: flex; align-items: center; }
  .brand__dot {
    border: 3px solid var(--blue);
    border-radius: 50%;
    flex: none;
  }
  .brand__name {
    color: var(--blue);
    font-weight: 500;
    letter-spacing: .04em;
    line-height: 1;
  }

  /* back side */
  .card--back { text-align: center; }
  .back__tagline {
    position: absolute; top: 46px; left: 0; right: 0;
    color: var(--blue); font-size: 14px; letter-spacing: .06em;
  }
  .back__brand {
    position: absolute; top: 140px; left: 0; right: 0;
    justify-content: center; gap: 16px;
  }
  .back__brand .brand__dot { width: 66px; height: 66px; }
  .back__brand .brand__name { font-size: 44px; }
  .back__url {
    position: absolute; bottom: 48px; left: 0; right: 0;
    color: var(--yellow); font-size: 14px; letter-spacing: .05em;
  }

  /* front side */
  .front__decor {
    position: absolute; right: -120px; top: 70px;
    width: 400px; height: 400px;
  }
  .front__brand {
    position: absolute; top: 44px; left: 52px; gap: 10px;
  }
  .front__brand .brand__dot { width: 42px; height: 42px; }
  .front__brand .brand__name { font-size: 30px; }
  .front__person { position: absolute; top: 140px; left: 52px; }
  .person__name { color: var(--yellow); font-weight: 700; font-size: 22px; letter-spacing: .02em; }
  .person__role { color: var(--blue); font-size: 15px; margin-top: 2px; }
  .person__rule { width: 16px; height: 2px; background: var(--blue); margin-top: 10px; }
  .contact { position: absolute; top: 232px; left: 52px; list-style: none; }
  .contact__row {
    display: flex; align-items: center; gap: 12px;
    color: var(--white); font-size: 15px; letter-spacing: .02em;
    height: 26px;
  }
  .contact__icon { width: 16px; height: 16px; flex: none; }
</style>
</head>
<body>

  <section class="card card--back" aria-label="Business card, back side">
    <p class="back__tagline">Executive Coaching and Human Capital Strategy</p>
    <div class="brand back__brand">
      <span class="brand__dot"></span>
      <span class="brand__name">MARROWFIELD</span>
    </div>
    <p class="back__url">www.marrowfield.example</p>
    <div class="card__band"></div>
  </section>

  <section class="card card--front" aria-label="Business card, front side">
    <svg class="front__decor" viewBox="0 0 400 400" aria-hidden="true">
      <circle cx="200" cy="200" r="185" fill="none" stroke="#1d2a33" stroke-width="10"/>
    </svg>
    <div class="brand front__brand">
      <span class="brand__dot"></span>
      <span class="brand__name">MARROWFIELD</span>
    </div>
    <div class="front__person">
      <p class="person__name">Idalia Renvoort</p>
      <p class="person__role">Principal</p>
      <div class="person__rule"></div>
    </div>
    <ul class="contact">
      <li class="contact__row">
        <svg class="contact__icon" viewBox="0 0 16 16" aria-hidden="true">
          <circle cx="8" cy="8" r="8" fill="var(--blue)"/>
          <path d="M5.2 4.2l1.4 1.6-.8 1c.5 1.1 1.3 1.9 2.4 2.4l1-.8 1.6 1.4-.9 1.4C7.6 11 5 8.4 4.8 5.1z" fill="var(--card)"/>
        </svg>
        +1 555 274 9186
      </li>
      <li class="contact__row">
        <svg class="contact__icon" viewBox="0 0 16 16" aria-hidden="true">
          <circle cx="8" cy="8" r="8" fill="var(--blue)"/>
          <rect x="4" y="5.2" width="8" height="5.6" fill="none" stroke="var(--card)" stroke-width="1.1"/>
          <path d="M4 5.4l4 3 4-3" fill="none" stroke="var(--card)" stroke-width="1.1"/>
        </svg>
        idalia@marrowfield.example
      </li>
      <li class="contact__row">
        <svg class="contact__icon" viewBox="0 0 16 16" aria-hidden="true">
          <circle cx="8" cy="8" r="8" fill="var(--blue)"/>
          <circle cx="8" cy="8" r="4" fill="none" stroke="var(--card)" stroke-width="1"/>
          <ellipse cx="8" cy="8" rx="1.8" ry="4" fill="none" stroke="var(--card)" stroke-width="1"/>
          <path d="M4 8h8" stroke="var(--card)" stroke-width="1"/>
        </svg>
        www.marrowfield.example
      </li>
    </ul>
    <div class="card__band"></div>
  </section>

</body>
</html>
```